Visitenkarten-Design für Handel mit Handstrickgarnen
Zielgruppe
Handel mit Handstrickgarnen, besonders Farbverläufe und handgefärbte Garne, aber auch Design von Strickmode. Die Zielgruppe sind alle, die gerne stricken oder häkeln, insbesondere Frauen aller Altersgruppen.
Aufgabenstellung
Schöne Farbverläufe bzw. Farbharmonien sind mir besonders wichtig und sollten insgesamt ins Auge stechen ohne jedoch zu grell bunt zu wirken. Sanft ineinander fließende Farben wären ideal, gerne auch etwas kräftigere Farben. Das Motiv des Logos könnte auch im Negativ sein auf dunklerem Hintergrund.

```html
<!DOCTYPE html>
<html lang="de">
<head>
<meta charset="utf-8">
<title>Lanavera – Visitenkarte</title>
<link href="https://fonts.googleapis.com/css2?family=Open+Sans:wght@400;600&display=swap" rel="stylesheet">
<style>
  :root {
    --paper: #ffffff;
    --ink: #111111;
    --frame: #555555;
    --blue: #3a55a4;
    --magenta: #c2185b;
    --copper: #c27a4a;
    --gold: #c8ad50;
    --olive: #8fa84a;
    --green: #008c5a;
    --teal: #0a7a8f;
    --rainbow: linear-gradient(90deg,
      var(--blue) 0%, var(--blue) 6%, var(--magenta) 22%, var(--copper) 38%,
      var(--gold) 53%, var(--olive) 68%, var(--green) 82%, var(--teal) 89%, var(--blue) 97%);
  }
  * { margin: 0; padding: 0; box-sizing: border-box; }
  html, body { width: 848px; height: 1200px; overflow: hidden; background: var(--paper); }
  body { position: relative; font-family: "Open Sans", Arial, sans-serif; color: var(--ink); }

  .card { position: absolute; left: 228px; width: 344px; height: 223px; }
  .card--front { top: 250px; border: 1px solid var(--frame); background: var(--paper); }
  .card--back { top: 509px; background: var(--rainbow); }

  .brand { position: absolute; display: flex; align-items: center; gap: 7px; font-weight: 600; }
  .brand__dot { border-radius: 50%; flex: none; }
  .card--front .brand { left: 0; right: 0; top: 42px; justify-content: center; font-size: 22px; color: var(--blue); letter-spacing: 0.5px; }
  .card--front .brand__dot { width: 16px; height: 16px; background: var(--magenta); }
  .card--back .brand { left: 0; right: 0; top: 92px; justify-content: center; font-size: 30px; color: var(--paper); letter-spacing: 0.5px; }
  .card--back .brand__dot { width: 22px; height: 22px; background: var(--paper); }

  .person { position: absolute; left: 18px; top: 118px; }
  .person__name {
    font-size: 12.5px; font-weight: 600; line-height: 1.1;
    background: linear-gradient(90deg, var(--blue), var(--magenta) 45%, var(--gold));
    -webkit-background-clip: text; background-clip: text; color: transparent; display: inline-block;
  }
  .person__role { font-size: 10px; line-height: 1.3; }

  .contact { position: absolute; top: 155px; font-size: 10px; line-height: 12.7px; }
  .contact--postal { left: 18px; }
  .contact--online { left: 134px; }

  .card__band { position: absolute; left: -1px; right: -1px; bottom: -1px; height: 12px; background: var(--rainbow); }
</style>
</head>
<body>
  <section class="card card--front">
    <div class="brand"><span class="brand__dot"></span><span class="brand__name">LANAVERA</span></div>
    <div class="person">
      <div class="person__name">Carla Beispiel</div>
      <div class="person__role">Geschäftsführerin</div>
    </div>
    <address class="contact contact--postal" style="font-style:normal">
      Wollweg 45<br>54321 Garnstadt<br>tel.: 05678 - 123 45
    </address>
    <address class="contact contact--online" style="font-style:normal">
      info@lanavera.de<br>www.lanavera.de
    </address>
    <div class="card__band"></div>
  </section>

  <section class="card card--back">
    <div class="brand"><span class="brand__dot"></span><span class="brand__name">LANAVERA</span></div>
  </section>
</body>
</html>
```